Velmora Water Purification

We need a website set up on a "Free account" WordPress platform. (This is the type of Wordpress site that you can sign up for and create online for free (not a server-hosted type.)
The website will be for a water purification company. They install devices in homes to purify the water for safer drinking, bathing, and cleaning.
Our logo is attached. Please keep color scheme of the website consistent with the logo.
Water Purification

```html
<!DOCTYPE html>
<html lang="en">
<head>
<meta charset="utf-8">
<title>Velmora Water Purification</title>
<link href="https://fonts.googleapis.com/css2?family=Roboto:wght@300;400;500;700&family=Roboto+Condensed:wght@400;700&display=swap" rel="stylesheet">
<style>
:root{
  --blue:#1a8ac9;
  --blue-deep:#1677b7;
  --blue-dark:#0f66a3;
  --navy:#1d3a56;
  --ink:#3a3a3a;
  --grey:#ececec;
  --grey-bg:#efefef;
  --orange:#ff5a0a;
  --teal:#14a4d9;
  --green:#6cb519;
  --charcoal:#3b3b3b;
  --white:#ffffff;
}
*{box-sizing:border-box;margin:0;padding:0}
html,body{width:1200px;height:3830px;overflow:hidden}
body{position:relative;font-family:"Roboto",Arial,sans-serif;color:var(--ink);background:var(--white)}
.abs{position:absolute}

/* top bar */
.topbar{left:0;top:0;width:1200px;height:46px;background:var(--blue-deep);color:var(--white);font-size:17px}
.social{left:46px;top:14px;display:flex;gap:7px}
.social span{width:17px;height:17px;background:var(--white);border-radius:3px}
.topbar .phone{left:190px;top:11px;display:flex;align-items:center;gap:8px;font-weight:500}
.topbar .help{left:958px;top:12px;font-size:14px}
.topbar .user{left:1050px;top:12px;font-size:14px;display:flex;gap:6px;align-items:center}

/* hero */
.hero{left:0;top:46px;width:1200px;height:1460px;overflow:hidden}
.hero-bg{position:absolute;inset:0;background:linear-gradient(180deg,#f4fbff 0%,#dcf0fb 20%,#8ccbed 34%,#3c9fd8 46%,#2b8fd0 72%,#4aa6dc 100%)}
.brand{left:46px;top:84px;display:flex;align-items:center;gap:14px}
.brand .dot{width:44px;height:44px;border-radius:50%;background:var(--blue)}
.brand .name{font-size:26px;font-weight:700;color:var(--blue-dark);line-height:1.1;width:220px}
.nav{left:645px;top:44px;display:flex;gap:30px;font-size:21px;color:var(--navy)}
.nav a{color:inherit;text-decoration:none;padding-bottom:8px}
.nav a.active{border-bottom:2px solid var(--navy)}
.eyebrow{left:327px;top:324px;font-size:20px;color:var(--navy);letter-spacing:.3px}
.headline{left:322px;top:344px;font-size:68px;font-weight:300;color:var(--navy)}
.headline-bold{left:600px;top:416px;font-size:70px;font-weight:700;color:var(--navy)}

.glass{left:36px;top:503px;width:1128px;height:868px;background:rgba(255,255,255,.14);border:1px solid rgba(255,255,255,.3)}
.sec-title{top:650px;font-size:50px;font-weight:300;color:var(--white)}
.sec-title b{font-weight:700}
.card{top:730px;width:447px;height:585px;background:rgba(214,238,252,.82);border-radius:8px}
.services{left:94px}
.contact{left:659px;width:444px}
.services .intro{left:26px;top:30px;width:400px;font-size:20px;line-height:1.25;color:var(--blue-dark)}
.services .intro b{font-weight:500;display:block}
.svc{left:32px;display:flex;gap:40px;align-items:flex-start}
.svc svg{flex:none}
.svc h3{font-size:27px;font-weight:700;color:var(--blue);margin-bottom:6px}
.svc p{font-size:13px;line-height:1.3;color:var(--blue-dark);width:270px}
.crow{left:46px;display:flex;gap:24px;align-items:flex-start;color:var(--blue-dark)}
.crow .big{font-size:42px;font-weight:500;line-height:1}
.crow .mid{font-size:26px;line-height:1.25}
.quote-label{left:46px;top:355px;font-size:26px;color:var(--blue-dark)}
.quote-input{left:46px;top:403px;width:349px;height:59px;background:#a9dcf6;border:1px solid #8fd0f2;font-size:18px;color:#5fb1dd;padding:18px 24px}
.quote-btn{left:46px;top:477px;width:189px;height:62px;background:var(--blue-deep);color:var(--white);font-size:26px;display:flex;align-items:center;justify-content:center}

/* pricing */
.section-title{width:1200px;text-align:center;font-weight:300}
.section-title b{font-weight:700}
.pricing-title{top:1560px;font-size:56px;color:var(--blue)}
.plan{top:1654px;width:261px;height:452px;background:var(--grey)}
.plan-head{height:159px;color:var(--white);text-align:center;padding-top:22px}
.plan-head .tier{font-size:20px}
.plan-head .price{font-size:42px;font-weight:300;margin-top:2px;position:relative}
.plan-head .price sup{font-size:12px;position:absolute;margin-left:-26px;top:12px}
.plan-head .order{margin:10px auto 0;width:200px;height:28px;background:var(--white);font-size:14px;line-height:28px}
.plan ul{list-style:none;text-align:center;font-size:14px;color:#777;margin-top:38px;line-height:31px}
.plan .more{position:absolute;bottom:26px;width:100%;text-align:center;font-size:14px;font-weight:700}
.basic .plan-head{background:var(--orange)} .basic .order,.basic .more{color:var(--orange)}
.regular .plan-head{background:var(--teal)} .regular .order,.regular .more{color:var(--teal)}
.premium .plan-head{background:var(--green)} .premium .order,.premium .more{color:var(--green)}
.ultimate .plan-head{background:var(--charcoal)} .ultimate .order,.ultimate .more{color:var(--charcoal)}

/* different */
.different{left:0;top:2208px;width:1200px;height:492px;background:var(--blue-deep)}
.diff-title{top:2256px;font-size:56px;color:var(--white)}
.feat{display:flex;gap:24px;color:var(--white)}
.feat h4{font-family:"Roboto Condensed",Arial,sans-serif;font-size:25px;font-weight:700;margin-bottom:4px}
.feat p{font-size:16px;line-height:1.2;width:320px}

/* testimonials */
.testimonials{left:0;top:2700px;width:1200px;height:823px;background:var(--grey-bg)}
.testi-title{top:2770px;font-size:56px;color:var(--ink)}
.person{top:2885px;width:542px}
.photo{height:357px;display:flex;align-items:center;justify-content:center}
.photo.one{background:linear-gradient(135deg,#d3dde3,#b9c6cf 55%,#eef1f3)}
.photo.two{background:linear-gradient(135deg,#c9cfd4,#8e9aa4 55%,#dfe4e7)}
.play{width:74px;height:74px;border-radius:50%;border:5px solid var(--white);display:flex;align-items:center;justify-content:center}
.tag{height:90px;background:var(--blue-deep);color:var(--white);text-align:center;padding-top:12px}
.tag .nm{font-family:"Roboto Condensed",Arial,sans-serif;font-size:34px;font-weight:700}
.tag .rl{font-size:20px}
.readmore{left:510px;top:3398px;width:180px;height:51px;background:var(--blue-deep);color:var(--white);font-family:"Roboto Condensed",Arial,sans-serif;font-weight:700;font-size:23px;display:flex;align-items:center;justify-content:center}

/* footer */
.footer{left:0;top:3523px;width:1200px;height:307px;background:var(--blue-dark)}
.subscribe{left:301px;top:3607px;width:598px;height:69px;border:2px solid var(--white);border-radius:4px;color:#bfe0f4;font-size:16px;padding:23px 26px}
.subscribe svg{position:absolute;right:24px;top:18px}
.copyright{top:3745px;font-size:19px;color:var(--white);text-align:center;width:1200px}
</style>
</head>
<body>

<header class="abs topbar">
  <div class="abs social"><span></span><span></span><span></span><span></span></div>
  <div class="abs phone">
    <svg width="20" height="20" viewBox="0 0 24 24"><path fill="#fff" d="M6.6 10.8a15 15 0 006.6 6.6l2.2-2.2a1 1 0 011-.25 11.4 11.4 0 003.6.57 1 1 0 011 1V20a1 1 0 01-1 1A17 17 0 013 4a1 1 0 011-1h3.5a1 1 0 011 1c0 1.25.2 2.45.57 3.57a1 1 0 01-.25 1z"/></svg>
    (480) 555-0192
  </div>
  <div class="abs help">? Help</div>
  <div class="abs user"><svg width="20" height="20" viewBox="0 0 20 20"><circle cx="10" cy="10" r="8.5" fill="none" stroke="#fff" stroke-width="1.6"/><circle cx="10" cy="8" r="3" fill="#fff"/><path d="M4.5 15.5c1.5-2.5 9.5-2.5 11 0" stroke="#fff" stroke-width="1.6" fill="none"/></svg>Aron T. Vale</div>
</header>

<section class="abs hero">
  <div class="hero-bg" role="img" aria-label="Blue water splash artwork with bubbles flowing across the header"></div>

  <div class="abs brand"><span class="dot"></span><span class="name">Velmora Water Purification</span></div>
  <nav class="abs nav">
    <a class="active" href="#">HOME</a><a href="#">SERVICES</a><a href="#">PRICING</a><a href="#">BLOG</a><a href="#">ABOUT US</a>
  </nav>

  <div class="abs eyebrow">VELMORA WATER PURIFICATION</div>
  <div class="abs headline">Feel the fresh of</div>
  <div class="abs headline-bold">Nature</div>

  <div class="abs glass"></div>
  <h2 class="abs sec-title" style="left:94px">Our <b>Services</b></h2>
  <h2 class="abs sec-title" style="right:97px">Contact <b>Us</b></h2>

  <div class="abs card services">
    <p class="abs intro"><b>Velmora Water Purification</b>is experienced more than 15 years in water purification solutions. We install devices in homes to purify the water for some purposes:</p>
    <div class="abs svc" style="top:195px">
      <svg width="60" height="86" viewBox="0 0 60 86"><path d="M4 4h52l-7 78H11z" fill="none" stroke="#1677b7" stroke-width="5"/><path d="M9 38h42" stroke="#1677b7" stroke-width="4"/></svg>
      <div><h3>Safer Drinking</h3><p>Lorem ipsum dolor sit amet, consectetur adipiscing elit, sed do eiusmod tempor incididunt ut labore et dolore magna aliqua.</p></div>
    </div>
    <div class="abs svc" style="top:325px">
      <svg width="60" height="86" viewBox="0 0 60 86"><path d="M30 2v14M8 42a22 22 0 0144 0z" fill="none" stroke="#1677b7" stroke-width="5"/><path d="M6 42h48M16 54v24M26 54v24M36 54v24M46 54v24" stroke="#1677b7" stroke-width="4"/></svg>
      <div><h3>Fresh Bathing</h3><p>Lorem ipsum dolor sit amet, consectetur adipiscing elit, sed do eiusmod tempor incididunt ut labore et dolore magna aliqua.</p></div>
    </div>
    <div class="abs svc" style="top:460px">
      <svg width="60" height="86" viewBox="0 0 60 86"><rect x="4" y="6" width="52" height="74" rx="4" fill="none" stroke="#1677b7" stroke-width="5"/><path d="M4 22h52" stroke="#1677b7" stroke-width="4"/><circle cx="30" cy="50" r="15" fill="none" stroke="#1677b7" stroke-width="5"/></svg>
      <div><h3>All Cleaning</h3><p>Lorem ipsum dolor sit amet, consectetur adipiscing elit, sed do eiusmod tempor incididunt ut labore et dolore magna aliqua.</p></div>
    </div>
  </div>

  <div class="abs card contact">
    <div class="abs crow" style="top:42px">
      <svg width="40" height="42" viewBox="0 0 24 24"><path fill="#1677b7" d="M6.6 10.8a15 15 0 006.6 6.6l2.2-2.2a1 1 0 011-.25 11.4 11.4 0 003.6.57 1 1 0 011 1V20a1 1 0 01-1 1A17 17 0 013 4a1 1 0 011-1h3.5a1 1 0 011 1c0 1.25.2 2.45.57 3.57a1 1 0 01-.25 1z"/></svg>
      <span class="big">555-0134 789</span>
    </div>
    <div class="abs crow" style="top:118px">
      <svg width="40" height="34" viewBox="0 0 40 34"><rect width="40" height="34" rx="3" fill="#1677b7"/><path d="M4 6l16 13 16-13" fill="none" stroke="#fff" stroke-width="3"/></svg>
      <span class="mid">service@velmora.com</span>
    </div>
    <div class="abs crow" style="top:192px">
      <svg width="40" height="36" viewBox="0 0 40 36"><path d="M20 2L2 18h6v16h9V24h6v10h9V18h6z" fill="#1677b7"/></svg>
      <span class="mid">Street Name<br>Address Line1<br>Address Line 2</span>
    </div>
    <div class="abs quote-label">Request Quotes</div>
    <div class="abs quote-input">Your email here</div>
    <div class="abs quote-btn">Request</div>
  </div>
</section>

<h2 class="abs section-title pricing-title">Plan &amp; <b>Pricing</b></h2>
<div class="abs plan basic" style="left:46px">
  <div class="plan-head"><div class="tier">Basic</div><div class="price"><sup>$</sup>399</div><div class="order">Order Now</div></div>
  <ul><li>Installation</li><li>Filter</li><li>Items 2</li><li>Items 3</li><li>Item Items 4</li><li>Item item Items 5</li></ul>
  <div class="more">Read more</div>
</div>
<div class="abs plan regular" style="left:329px">
  <div class="plan-head"><div class="tier">Regular</div><div class="price"><sup>$</sup>499</div><div class="order">Order Now</div></div>
  <ul><li>Installation</li><li>Filter</li><li>Items 2</li><li>Items 3</li><li>Item Items 4</li><li>Item item Items 5</li></ul>
  <div class="more">Read more</div>
</div>
<div class="abs plan premium" style="left:612px">
  <div class="plan-head"><div class="tier">Premium</div><div class="price"><sup>$</sup>699</div><div class="order">Order Now</div></div>
  <ul><li>Installation</li><li>Filter</li><li>Items 2</li><li>Items 3</li><li>Item Items 4</li><li>Item item Items 5</li></ul>
  <div class="more">Read more</div>
</div>
<div class="abs plan ultimate" style="left:893px">
  <div class="plan-head"><div class="tier">Ultimate</div><div class="price"><sup>$</sup>899</div><div class="order">Order Now</div></div>
  <ul><li>Installation</li><li>Filter</li><li>Items 2</li><li>Items 3</li><li>Item Items 4</li><li>Item item Items 5</li></ul>
  <div class="more">Read more</div>
</div>

<section class="abs different"></section>
<h2 class="abs section-title diff-title">What make us <b>different</b>?</h2>
<div class="abs feat" style="left:118px;top:2370px">
  <svg width="80" height="80" viewBox="0 0 80 80"><path d="M14 34a27 27 0 0148-10" fill="none" stroke="#fff" stroke-width="10"/><path d="M66 12v22H44z" fill="#fff"/><path d="M66 46a27 27 0 01-48 10" fill="none" stroke="#fff" stroke-width="10"/><path d="M14 68V46h22z" fill="#fff"/></svg>
  <div><h4>Long Life Material</h4><p>If we are unable to deliver anything that we say we can we will refund you 100% of your investment.</p></div>
</div>
<div class="abs feat" style="left:620px;top:2370px">
  <svg width="84" height="84" viewBox="0 0 84 84"><rect x="6" y="38" width="16" height="40" fill="#fff"/><path d="M28 40l14-30c8 0 10 6 8 14l-3 10h22c6 0 8 6 6 10l-8 30H28z" fill="none" stroke="#fff" stroke-width="6" stroke-linejoin="round"/></svg>
  <div><h4>Quality Assurance</h4><p>After 12 months of on time payments - Customers will receive cash back reward bonuses</p></div>
</div>
<div class="abs feat" style="left:118px;top:2508px">
  <svg width="80" height="80" viewBox="0 0 80 80"><circle cx="40" cy="40" r="33" fill="none" stroke="#fff" stroke-width="7"/><path d="M40 20v22H56" fill="none" stroke="#fff" stroke-width="7"/></svg>
  <div><h4>24/7 Support</h4><p>24/7 U.S. Based Customer Support Phone and Email</p></div>
</div>
<div class="abs feat" style="left:620px;top:2508px">
  <svg width="84" height="84" viewBox="0 0 84 84"><circle cx="32" cy="44" r="18" fill="none" stroke="#fff" stroke-width="12" stroke-dasharray="7 5"/><circle cx="32" cy="44" r="9" fill="none" stroke="#fff" stroke-width="5"/><circle cx="64" cy="20" r="11" fill="none" stroke="#fff" stroke-width="8" stroke-dasharray="5 4"/><circle cx="64" cy="66" r="11" fill="none" stroke="#fff" stroke-width="8" stroke-dasharray="5 4"/></svg>
  <div><h4>High Efficiency System</h4><p>Do you need us to come to your office to help train staff? That's not a problem. We will come to you and provide hands on training.</p></div>
</div>

<section class="abs testimonials"></section>
<h2 class="abs section-title testi-title">What people say <b>about us</b>?</h2>
<div class="abs person" style="left:46px">
  <div class="photo one" role="img" aria-label="Video testimonial photo of a smiling businesswoman in an office">
    <div class="play"><svg width="28" height="32" viewBox="0 0 28 32"><path d="M4 2l22 14L4 30z" fill="#fff"/></svg></div>
  </div>
  <div class="tag"><div class="nm">Mira L. Quinn</div><div class="rl">CEO of Brightlane</div></div>
</div>
<div class="abs person" style="left:612px">
  <div class="photo two" role="img" aria-label="Video testimonial photo of a businessman seated at a desk with a laptop">
    <div class="play"><svg width="28" height="32" viewBox="0 0 28 32"><path d="M4 2l22 14L4 30z" fill="#fff"/></svg></div>
  </div>
  <div class="tag"><div class="nm">Aron T. Vale</div><div class="rl">CEO of Brightlane</div></div>
</div>
<div class="abs readmore">READ MORE</div>

<footer class="abs footer"></footer>
<div class="abs subscribe">Enter your email to subscribe...
  <svg width="40" height="32" viewBox="0 0 40 32"><rect width="40" height="32" rx="3" fill="#fff"/><path d="M4 6l16 12 16-12" fill="none" stroke="#0f66a3" stroke-width="3"/></svg>
</div>
<p class="abs copyright">Copyright 2017 Velmora Water Purifier. All rights reserved.</p>

</body>
</html>
```